Small environmental consultancy requires basic yet awesome website design by aspiring and cool desig

We are a small environmental consultancy based in Australia, we have set-out a design brief for our website, using a logo we had completed here on Mosaic Yard as well. We hope you can help us with a website!

Website must be pagelark friendly - we have reserved hosting with them already!

Number of Pages Required

4 page

Requirements
Must have
• use supplied logo
• pagelark
• follow provided brief

```html
<!DOCTYPE html>
<html lang="en">
<head>
<meta charset="utf-8">
<title>Greenfield Advisory</title>
<link href="https://fonts.googleapis.com/css2?family=Open+Sans:wght@400;600;700&family=Oswald:wght@400;500&display=swap" rel="stylesheet">
<style>
:root{
  --green:#8db33a;
  --green-dark:#6f9226;
  --footer:#a0bd4c;
  --ink:#3d3d3d;
  --muted:#7a7a7a;
  --band:#ededed;
  --line:#d9d9d9;
  --base:#333333;
  --white:#ffffff;
  --hero-top:#7fb0de;
  --hero-bottom:#9cbf6a;
}
*{box-sizing:border-box;margin:0;padding:0}
html,body{width:736px;height:1200px;overflow:hidden}
body{font-family:"Open Sans",Arial,sans-serif;color:var(--ink);background:var(--white);position:relative}
.site-header{height:80px;display:flex;align-items:center;padding:0 22px;position:relative}
.brand{display:flex;align-items:center;gap:8px}
.brand-mark{width:34px;height:34px;border-radius:50%;background:var(--green)}
.brand-name{font-size:15px;font-weight:700;color:var(--green-dark);line-height:1.05}
.brand-name span{display:block;font-size:11px;padding-left:36px}
.main-nav{display:flex;margin-left:auto;margin-right:26px}
.main-nav a{font-size:9px;font-weight:600;color:var(--ink);text-decoration:none;padding:30px 10px;text-transform:uppercase;border-top:3px solid transparent}
.main-nav a.is-active{color:var(--green);border-top-color:var(--green)}
.phone{display:flex;align-items:center;gap:5px;font-size:11px;font-weight:600;color:var(--ink)}
.hero{position:absolute;left:22px;top:88px;width:692px;height:322px;background:linear-gradient(180deg,var(--hero-top),var(--hero-bottom));box-shadow:0 2px 6px rgba(0,0,0,.25)}
.hero-caption{position:absolute;left:0;top:128px;width:305px;background:rgba(141,179,58,.85);padding:9px 14px;color:var(--white);font-family:"Oswald",Arial,sans-serif;text-transform:uppercase}
.hero-caption h1{font-size:18px;font-weight:400;letter-spacing:.3px}
.hero-caption p{font-size:12px;letter-spacing:.3px}
.hero-dots{position:absolute;left:14px;bottom:10px;display:flex;gap:4px}
.hero-dots i{width:6px;height:6px;border-radius:50%;background:rgba(255,255,255,.6)}
.hero-dots i:first-child{background:var(--white)}
.welcome{position:absolute;top:443px;left:0;width:736px;text-align:center}
.welcome h2{font-size:15px;font-weight:700;color:var(--ink);text-transform:uppercase}
.welcome h2 span{color:var(--green)}
.welcome p{margin:10px auto 0;width:620px;font-size:8.5px;line-height:1.5;color:var(--muted)}
.services{position:absolute;top:535px;left:0;width:736px;height:210px;background:var(--band)}
.section-title{display:flex;align-items:center;gap:8px;font-size:11px;font-weight:700;text-transform:uppercase;color:var(--ink)}
.section-title span{color:var(--green)}
.section-title::after{content:"";flex:1;height:1px;background:var(--line)}
.services .section-title{position:absolute;left:22px;right:22px;top:16px}
.service-list{position:absolute;left:22px;top:42px;display:flex;gap:13px}
.service-card{width:222px;background:var(--white);box-shadow:0 1px 3px rgba(0,0,0,.15)}
.service-photo{height:132px}
.service-card p{font-size:7.5px;font-weight:700;text-transform:uppercase;text-align:center;padding:5px 0;color:var(--ink)}
.people{position:absolute;top:768px;left:22px;width:440px}
.person-list{display:flex;gap:22px;margin-top:16px}
.person{display:flex;gap:10px;width:209px}
.person-photo{width:62px;height:62px;border-radius:50%;flex:none;background:radial-gradient(circle,#c9a489,#7d6a5c);border:2px solid var(--white);box-shadow:0 0 0 1px var(--line)}
.person h3{font-size:7.5px;font-weight:700;text-transform:uppercase;margin-top:4px}
.person p{font-size:6.5px;line-height:1.5;color:var(--muted);margin-top:4px}
.news{position:absolute;top:768px;left:490px;width:224px}
.news .section-title::after{order:2}
.news .section-title svg{order:3}
.news-item{display:flex;gap:8px;margin-top:14px}
.news-date{width:30px;height:30px;border:1px solid var(--line);text-align:center;font-size:7px;line-height:1.2;padding-top:4px;flex:none;color:var(--muted)}
.news-date b{display:block;font-size:10px;color:var(--ink)}
.news-item h4{font-size:7px;font-weight:700;color:var(--green);text-transform:uppercase}
.news-item p{font-size:6.5px;color:var(--muted);margin-top:3px;line-height:1.4}
.clients{position:absolute;top:918px;left:22px;width:692px;height:72px;display:flex;justify-content:space-around;align-items:center;border-top:1px solid var(--line)}
.client{display:flex;align-items:center;gap:5px;font-size:10px;font-weight:700;color:var(--green-dark)}
.client i{width:12px;height:12px;background:var(--green-dark);display:block}
.site-footer{position:absolute;top:1010px;left:0;width:736px;height:155px;background:var(--footer);color:var(--white);display:flex;gap:22px;padding:22px 22px 0}
.footer-col h5{font-size:8px;font-weight:700;text-transform:uppercase;margin-bottom:8px}
.footer-col ul{list-style:none}
.footer-col li{font-size:7px;line-height:1.9}
.footer-col p{font-size:7px;line-height:1.6}
.col-links{width:100px}
.col-quote{width:170px}
.col-news{width:150px}
.field{margin-top:8px;height:16px;background:var(--white);color:var(--muted);font-size:7px;padding:3px 5px}
.subscribe{margin-top:6px;display:inline-block;background:var(--base);font-size:7px;padding:3px 8px;text-transform:uppercase}
.social li{display:flex;align-items:center;gap:6px;margin-bottom:4px}
.social i{width:14px;height:14px;border-radius:50%;background:var(--white);display:block}
.copyright{position:absolute;top:1165px;left:0;width:736px;height:35px;background:var(--base);color:#bdbdbd;font-size:7.5px;display:flex;align-items:center;justify-content:center}
</style>
</head>
<body>
<header class="site-header">
  <div class="brand"><div class="brand-mark"></div><div class="brand-name">Greenfield<span>Advisory</span></div></div>
  <nav class="main-nav">
    <a class="is-active" href="#">Home</a><a href="#">Services</a><a href="#">People</a><a href="#">Clients</a><a href="#">Contact</a>
  </nav>
  <div class="phone">
    <svg width="11" height="11" viewBox="0 0 24 24"><path fill="#8db33a" d="M6.6 10.8a15 15 0 0 0 6.6 6.6l2.2-2.2c.3-.3.7-.4 1-.2 1.1.4 2.3.6 3.6.6.6 0 1 .4 1 1V20c0 .6-.4 1-1 1A17 17 0 0 1 3 4c0-.6.4-1 1-1h3.5c.6 0 1 .4 1 1 0 1.2.2 2.4.6 3.6.1.3 0 .7-.2 1z"/></svg>
    + 0800 555 010 20
  </div>
</header>

<section class="hero" role="img" aria-label="Photo of balanced stacked pebbles held by a hand over grass under a blue sky">
  <div class="hero-caption"><h1>Environmental Consultancy</h1><p>Project Management</p></div>
  <div class="hero-dots"><i></i><i></i><i></i><i></i></div>
</section>

<section class="welcome">
  <h2>Welcome to <span>Greenfield Advisory</span></h2>
  <p>Lorem Ipsum has been the industry's standard dummy text ever since the 1500s, when an unknown printer took a galley of type and scrambled it to make a type specimen book. It has survived not only five centuries, but also the leap into electronic typesetting, remaining essentially unchanged.</p>
</section>

<section class="services">
  <div class="section-title">Our <span>Service</span></div>
  <div class="service-list">
    <article class="service-card"><div class="service-photo" role="img" aria-label="Photo of cupped hands holding soil with a green seedling" style="background:linear-gradient(160deg,#8fbf55,#5d7f34)"></div><p>Risk Appraisal</p></article>
    <article class="service-card"><div class="service-photo" role="img" aria-label="Photo of a team meeting around a laptop" style="background:linear-gradient(160deg,#e4eef2,#8fb0bd)"></div><p>Scope Investment and Staging</p></article>
    <article class="service-card"><div class="service-photo" role="img" aria-label="Photo of business people shaking hands in an office" style="background:linear-gradient(160deg,#d8dde2,#65707c)"></div><p>Technical Specifications</p></article>
  </div>
</section>

<section class="people">
  <div class="section-title"><span>People</span></div>
  <div class="person-list">
    <div class="person"><div class="person-photo" role="img" aria-label="Portrait photo of Liam Parker"></div><div><h3>Liam Parker</h3><p>Senior consultant with over fifteen years guiding site assessments, approvals and rehabilitation programs across regional and coastal projects.</p></div></div>
    <div class="person"><div class="person-photo" role="img" aria-label="Portrait photo of Owen Hartley"></div><div><h3>Owen Hartley</h3><p>Project manager focused on water quality, environmental planning and compliance reporting for councils, utilities and private developers.</p></div></div>
  </div>
</section>

<section class="news">
  <div class="section-title">Latest <span>News</span>
    <svg width="18" height="8" viewBox="0 0 18 8"><path d="M5 1 2 4l3 3M13 1l3 3-3 3" fill="none" stroke="#7a7a7a" stroke-width="1.2"/></svg>
  </div>
  <div class="news-item"><div class="news-date"><b>28</b>Jan</div><div><h4>New Guidelines Released</h4><p>Updated site assessment rules now apply across the state.</p></div></div>
  <div class="news-item"><div class="news-date"><b>14</b>Jan</div><div><h4>Field Survey Season</h4><p>Our team begins spring monitoring at four river sites.</p></div></div>
</section>

<section class="clients">
  <div class="client"><i></i>Riverbend Water</div>
  <div class="client"><i></i>Nullaroo Trust</div>
  <div class="client"><i></i>Karri Group</div>
  <div class="client"><i></i>Tallow Shire</div>
  <div class="client"><i></i>Stonegate Build</div>
  <div class="client"><i></i>Ferro Line</div>
</section>

<footer class="site-footer">
  <div class="footer-col col-links"><h5>Quick Links</h5><ul><li>Home</li><li>About Us</li><li>Services</li><li>Testimonials</li><li>Contact Us</li></ul></div>
  <div class="footer-col col-links"><h5>Support Links</h5><ul><li>Overview</li><li>Careers</li><li>Our Team</li><li>Privacy Policy</li><li>Terms of Use</li></ul></div>
  <div class="footer-col col-quote"><h5>Client's Testimonials</h5><p>Clear advice, sound reports and a team that delivered every milestone on time. We would gladly work with them again.</p><p>— Regional Water Board</p></div>
  <div class="footer-col col-news"><h5>Newsletter Sign Up</h5><p>Sign up to receive our latest news and project updates.</p><div class="field">Email address</div><span class="subscribe">Subscribe</span></div>
  <div class="footer-col"><h5>Follow Us</h5><ul class="social"><li><i></i>Join us</li><li><i></i>Follow</li><li><i></i>Connect</li></ul></div>
</footer>
<div class="copyright">Copyright © 2013 - All Rights Reserved</div>
</body>
</html>
```